Packing for Razor Blade VORELIN

Dears: We need a packing design. The product is an Disposable Razor Blade. We are a company in Brazil.

The packing consists in a bag package which the Disposables Razos are placed. 5 units into each bag.

The bag is not 100% printed and should let a space to the customer see the razors inside. Some competitors uses oval circle. I attached competitor package (Tove Marigold)

The background color should be blue, this color tonality should vary its magnitude from dark blue to soft blue. Blue is a good color for personal care products because customer can take the impression of cleanness, especially for razor blade which has the fuction to shave.

You can feel free to add other colors however it can not be much colorfull because it may get trouble to printer company print it. Silver is good.

You can feel free to do details. You can feel free also to place the logo above the package or at bottom of it.

Dimmensions:
Heigh 24cm
Width 10cm

Featuring
- Featuring: Handle with Grip. In Portuguese - (Cabo Aderente)
- Featuring: 2 Razors. In portuguese - (Duas Lâminas)

Reason: I stayed many days with out providing feedbacks. I want to give more time for you .

Target Market(s)

Mans ( for woman we will design other package )

Requirements
Nice to have
• maybe some tears as a wet surface...
pls can feel free

```html
<!DOCTYPE html>
<html lang="en">
<head>
<meta charset="utf-8">
<title>VORELIN Disposable Razor Pack</title>
<link rel="stylesheet" href="https://fonts.googleapis.com/css2?family=Anton&family=Roboto:wght@400&display=swap">
<style>
  :root {
    --navy-deep: #02124a;
    --navy: #06268f;
    --blue-mid: #0a56c9;
    --blue-bright: #1f8ff0;
    --blue-soft: #6cc4ff;
    --silver-light: #f2f2f2;
    --silver-mid: #b9b9b9;
    --silver-dark: #7d7d7d;
    --window-white: #ffffff;
    --window-tint: #dfeaf7;
    --ink: #0a1440;
    --logo-white: #f4f7ff;
  }
  html, body {
    margin: 0;
    padding: 0;
    width: 1200px;
    height: 2880px;
    overflow: hidden;
    background: #ffffff;
  }
  .pack {
    display: block;
    width: 1200px;
    height: 2880px;
  }
  .brand-name {
    font-family: "Anton", "Impact", sans-serif;
    font-size: 150px;
    letter-spacing: 10px;
    fill: var(--logo-white);
  }
  .feature-lead {
    font-family: "Anton", "Impact", sans-serif;
    font-size: 56px;
    fill: var(--ink);
  }
  .feature-title {
    font-family: "Anton", "Impact", sans-serif;
    font-size: 122px;
    fill: var(--ink);
    stroke: var(--silver-light);
    stroke-width: 6px;
    paint-order: stroke;
  }
  .feature-translation {
    font-family: "Roboto", "Arial", sans-serif;
    font-size: 40px;
    fill: var(--ink);
  }
</style>
</head>
<body>
<svg class="pack" viewBox="0 0 1200 2880" xmlns="http://www.w3.org/2000/svg">
  <defs>
    <linearGradient id="bg-top" x1="0" y1="0" x2="0" y2="1">
      <stop offset="0" stop-color="var(--navy-deep)"/>
      <stop offset="1" stop-color="var(--navy)"/>
    </linearGradient>
    <radialGradient id="bg-lower" cx="0.55" cy="0.55" r="0.75">
      <stop offset="0" stop-color="var(--blue-soft)"/>
      <stop offset="0.45" stop-color="var(--blue-bright)"/>
      <stop offset="1" stop-color="var(--navy)"/>
    </radialGradient>
    <linearGradient id="silver-band" x1="0" y1="0" x2="0" y2="1">
      <stop offset="0" stop-color="var(--silver-light)"/>
      <stop offset="0.5" stop-color="var(--silver-mid)"/>
      <stop offset="1" stop-color="var(--silver-dark)"/>
    </linearGradient>
    <radialGradient id="window-fill" cx="0.5" cy="0.5" r="0.5">
      <stop offset="0.8" stop-color="var(--window-white)"/>
      <stop offset="1" stop-color="var(--window-tint)"/>
    </radialGradient>
    <linearGradient id="product-fill" x1="0" y1="0" x2="1" y2="1">
      <stop offset="0" stop-color="var(--blue-mid)"/>
      <stop offset="1" stop-color="var(--navy)"/>
    </linearGradient>
    <filter id="window-glow" x="-10%" y="-10%" width="120%" height="120%">
      <feGaussianBlur stdDeviation="18"/>
    </filter>
  </defs>

  <!-- background: wet blue surface -->
  <rect class="background-lower" width="1200" height="2880" fill="url(#bg-lower)"
        role="img" aria-label="Blue background covered with water droplets"/>
  <polygon class="background-top" points="0,0 1200,0 1200,468 0,816" fill="url(#bg-top)"
           role="img" aria-label="Dark blue background covered with water droplets"/>

  <!-- brand -->
  <text class="brand-name" x="600" y="318" text-anchor="middle">VORELIN</text>

  <!-- upper silver band -->
  <polygon class="band-upper" points="0,816 1200,468 1200,720 0,1092" fill="url(#silver-band)"/>

  <!-- clear product window -->
  <ellipse class="window-glow" cx="612" cy="1303" rx="520" ry="802" fill="#ffffff" opacity="0.7" filter="url(#window-glow)"/>
  <ellipse class="product-window" cx="612" cy="1303" rx="504" ry="787" fill="url(#window-fill)"/>

  <!-- product image area -->
  <rect class="product-image" x="72" y="1656" width="552" height="504" rx="40" fill="url(#product-fill)" opacity="0.9"
        role="img" aria-label="Two blue disposable twin-blade razors with grip handles"/>

  <!-- lower silver band -->
  <polygon class="band-lower" points="0,2208 1200,1992 1200,2424 0,2640" fill="url(#silver-band)"/>

  <!-- features -->
  <g class="features" transform="rotate(-10.2 600 2400)">
    <text class="feature-lead" x="150" y="2330">Featuring</text>
    <text class="feature-title" x="180" y="2470" textLength="820" lengthAdjust="spacingAndGlyphs">Handle with Grip</text>
    <text class="feature-title" x="180" y="2600" textLength="500" lengthAdjust="spacingAndGlyphs">2 Razors</text>
    <text class="feature-translation" x="710" y="2528">Cabo Aderente</text>
    <text class="feature-translation" x="710" y="2574">Duas Lâminas</text>
  </g>
</svg>
</body>
</html>
```